Larkspur Ridge Management - Business Cards

I need business cards. My current logo was designed by a designer at this site and I very much like and am happy with the results. I would like a business card that is trendy, unique, current yet professional. I deal with high net worth clients daily

Target Market(s)

Out of state investors looking to get into the rental market in Ohio

Industry/Entity Type

Property Management, Consulting

Contact Information for Business Card

Name, Title (Chief Financial Officer) office phone number (555) 817-3094 website address larkridgemgmt.example

Font styles to use
Sans Serif

Colors
0054AA
0677BA
7BADD7
CADEEF
E8F1F8
0094D4
00A9DD
6FCCEA
C7EBF8
E9F6FB
00AB8E
00BBA5
67D7C9
C6EFE9
E9F9F6

```html
<!DOCTYPE html>
<html lang="en">
<head>
<meta charset="utf-8">
<title>Larkspur Ridge Management – Business Card</title>
<link rel="stylesheet" href="https://fonts.googleapis.com/css2?family=Arimo:wght@700&display=swap">
<style>
  :root {
    --navy: #233457;
    --red: #c9282f;
    --red-dark: #a11d24;
    --white: #ffffff;
  }
  html, body {
    margin: 0;
    padding: 0;
    overflow: hidden;
    background: var(--white);
  }
  .card {
    position: relative;
    width: 1200px;
    height: 686px;
    overflow: hidden;
    background: var(--white);
    font-family: "Arimo", Arial, sans-serif;
    font-weight: 700;
    color: var(--white);
  }
  .card-shapes {
    position: absolute;
    inset: 0;
  }
  .brand-name {
    position: absolute;
    left: 40px;
    top: 250px;
    width: 420px;
    margin: 0;
    text-align: center;
    color: var(--navy);
    font-size: 46px;
    line-height: 1.15;
    text-transform: uppercase;
    letter-spacing: 1px;
  }
  .person-name {
    position: absolute;
    left: 589px;
    top: 108px;
    margin: 0;
    font-size: 96px;
    line-height: 1;
    letter-spacing: 1px;
  }
  .person-title {
    position: absolute;
    left: 717px;
    top: 220px;
    margin: 0;
    font-size: 40px;
    line-height: 1;
  }
  .contact-icon {
    position: absolute;
  }
  .icon-phone { left: 714px; top: 327px; width: 60px; height: 58px; }
  .icon-globe { left: 635px; top: 448px; width: 62px; height: 62px; }
  .icon-mail  { left: 793px; top: 552px; width: 62px; height: 42px; }
  .phone-number {
    position: absolute;
    left: 809px;
    top: 318px;
    font-size: 41px;
    line-height: 1;
  }
  .phone-label {
    position: absolute;
    left: 809px;
    top: 366px;
    font-size: 30px;
    line-height: 1;
  }
  .website {
    position: absolute;
    left: 721px;
    top: 458px;
    font-size: 37px;
    line-height: 1;
  }
  .email {
    position: absolute;
    right: 20px;
    top: 606px;
    font-size: 37px;
    line-height: 1;
    white-space: nowrap;
  }
</style>
</head>
<body>
<main class="card">
  <svg class="card-shapes" width="1200" height="686" viewBox="0 0 1200 686" aria-hidden="true">
    <polygon class="navy-panel" points="763,0 1200,0 1200,686 410,686" fill="var(--navy)"/>
    <polygon class="ribbon-fold" points="550,209 657,209 620,280" fill="var(--red-dark)"/>
    <rect class="name-ribbon" x="550" y="101" width="650" height="108" fill="var(--red)"/>
  </svg>

  <h2 class="brand-name">Larkspur Ridge<br>Management</h2>

  <h1 class="person-name">JOHN DOE</h1>
  <p class="person-title">Chief Financial Officer</p>

  <svg class="contact-icon icon-phone" viewBox="0 0 60 58" aria-hidden="true">
    <path d="M10 2 C4 4 0 9 1 17 C3 31 20 50 36 56 C43 58 48 54 51 49 L44 40 C42 38 39 38 37 40 L33 43 C25 38 19 31 15 23 L19 19 C21 17 21 14 19 12 Z" fill="var(--white)"/>
    <path d="M32 6 A20 20 0 0 1 54 28" fill="none" stroke="var(--white)" stroke-width="5" stroke-linecap="round"/>
    <path d="M31 16 A11 11 0 0 1 44 29" fill="none" stroke="var(--white)" stroke-width="5" stroke-linecap="round"/>
  </svg>
  <span class="phone-number">(555) 817-3094</span>
  <span class="phone-label">Office Call/Text</span>

  <svg class="contact-icon icon-globe" viewBox="0 0 62 62" aria-hidden="true">
    <circle cx="31" cy="31" r="31" fill="var(--white)"/>
    <ellipse cx="31" cy="31" rx="12" ry="29" fill="none" stroke="var(--navy)" stroke-width="3"/>
    <line x1="31" y1="2" x2="31" y2="60" stroke="var(--navy)" stroke-width="3"/>
    <line x1="2" y1="22" x2="60" y2="22" stroke="var(--navy)" stroke-width="3"/>
    <line x1="2" y1="40" x2="60" y2="40" stroke="var(--navy)" stroke-width="3"/>
  </svg>
  <span class="website">larkridgemgmt.example</span>

  <svg class="contact-icon icon-mail" viewBox="0 0 62 42" aria-hidden="true">
    <rect x="1.5" y="1.5" width="59" height="39" fill="none" stroke="var(--white)" stroke-width="3"/>
    <path d="M2 2 L31 26 L60 2" fill="none" stroke="var(--white)" stroke-width="3"/>
    <path d="M2 40 L22 20 M60 40 L40 20" fill="none" stroke="var(--white)" stroke-width="3"/>
  </svg>
  <span class="email">info@larkspurridgemgmt.example</span>
</main>
</body>
</html>
```